Tobias Webpage Design

I would like to start an business and management consultancy business. I am thinking to called it "Krelto Consultancy". Besides the consultancy services, I would also like to provide training on finance, forensic accounting, fraud prevention and internal control.
Professional management consultants are contracted by organizations to provide advisory services in an objective and independent manner.

Services include, but are not limited to, strategic planning, facilitation, quality assurance, education and training, investment counsel, identification and analysis of management problems, developing solutions, and the implementation of proposed solutions.

Professional management consultants are hired when an organization lacks sufficient resources, requires external objective advice, or because they have expertise not available within the client organization.

I would like to see the webpage design that use colors apple green with some other contrast color. The design have to be professional look but with a new age touch.

Reason: Unable to find a suitable web pages design

Dear all

Since last week I post a request, but till to date, I has yet to received a new sparkling creative and "wow" web page design. Please help me here!

Regards

Reason: Yet to found a suitable web designer for my web design. Help! I just need a fresh and professional look design. You may ignore the color code I prefer. Send me your sparkling creative work. Thank you so much!

Some examples

```html
<!DOCTYPE html>
<html lang="en">
<head>
<meta charset="utf-8">
<title>Krelto Consultancy</title>
<link href="https://fonts.googleapis.com/css2?family=Open+Sans:wght@400;600;700&family=Montserrat:wght@400;700&display=swap" rel="stylesheet">
<style>
:root{
  --green:#6aa136;
  --green-dark:#4f7f25;
  --red:#c9322a;
  --grey-bg:#e4e6e6;
  --grey-hex:#c8cacb;
  --text:#4a4a4a;
  --muted:#8c8c8c;
  --white:#ffffff;
  --footer-bottom:#3f6a1c;
}
*{box-sizing:border-box;margin:0;padding:0}
html,body{width:720px;height:1200px;overflow:hidden}
body{font-family:"Open Sans",Arial,sans-serif;color:var(--text);background:#fff;font-size:9px}
.wrap{width:590px;margin:0 auto;position:relative}
.topbar{background:var(--green);height:16px;color:#fff;font-size:8px}
.topbar .wrap{display:flex;justify-content:flex-end;gap:18px;align-items:center;height:16px}
.topbar span{display:flex;align-items:center;gap:4px}
.header{height:74px}
.header .wrap{display:flex;justify-content:space-between;align-items:center;height:74px}
.logo{font-family:"Montserrat",sans-serif;font-weight:700;color:#333;line-height:1;display:flex;align-items:center;gap:8px}
.logo .mark{width:12px;height:12px;background:var(--green)}
.logo .name{font-size:22px;letter-spacing:1px}
.logo .sub{display:block;font-size:10px;font-weight:400;color:var(--green);letter-spacing:2px;margin-top:3px}
.nav{display:flex;font-size:8px;font-weight:700;color:#444}
.nav a{padding:6px 12px;border-left:1px solid #ccc;text-decoration:none;color:inherit}
.nav a:first-child{border-left:none}
.hero{height:240px;position:relative;background:linear-gradient(100deg,#9fa7ad 0%,#c9ccd0 35%,#e8eaec 60%,#b9c0c4 100%)}
.hero .wrap{height:240px}
.hero h1{position:absolute;left:0;top:140px;font-family:"Montserrat",sans-serif;font-weight:400;color:#fff;font-size:20px;line-height:1.15;text-transform:uppercase}
.btn{display:inline-block;color:#fff;font-size:8px;font-weight:700;text-transform:uppercase;padding:9px 18px;border-radius:2px}
.btn-green{background:var(--green);position:absolute;left:0;top:195px}
.btn-red{background:var(--red);padding:9px 26px}
.dots{position:absolute;left:50%;bottom:14px;transform:translateX(-50%);display:flex;gap:5px}
.dots i{width:6px;height:6px;border-radius:50%;background:rgba(255,255,255,.6)}
.dots i:first-child{background:#fff}
.services{background:var(--grey-bg);height:400px;padding-top:28px}
.sec-head{display:flex;justify-content:space-between;align-items:center}
h2{font-family:"Montserrat",sans-serif;font-weight:400;font-size:15px;color:#555;text-transform:uppercase}
.search{width:140px;height:16px;background:#fff;border:1px solid #ccc;display:flex;justify-content:space-between;align-items:center;padding:0 5px;color:#aaa;font-size:7px}
.svc-grid{display:flex;justify-content:space-between;margin-top:18px}
.svc{width:130px;text-align:center}
.hex{position:relative;width:94px;height:108px;margin:0 auto}
.hex svg{position:absolute;inset:0}
.hex span{position:relative;display:flex;height:100%;align-items:center;justify-content:center;color:#fff;font-weight:700;font-size:10px;line-height:1.2;padding:0 10px}
.svc p{margin-top:18px;font-size:7.5px;line-height:1.55;color:#444}
.svc.dim p{color:#aaa}
.center{text-align:center;margin-top:70px}
.testimonials{padding-top:30px;height:370px}
.quotes{display:grid;grid-template-columns:1fr 1fr;column-gap:40px;row-gap:26px;margin-top:16px}
.quote p{font-size:7.5px;line-height:1.55;font-style:italic;color:#555}
.quote .who{text-align:right;color:var(--green);font-weight:700;font-size:7.5px;margin-top:4px}
.testimonials .center{margin-top:34px}
.footer{background:var(--green);color:#fff;height:94px;padding-top:12px;font-size:7px}
.footer .wrap{display:flex;justify-content:space-between}
.f-links{display:flex;gap:9px;font-weight:600}
.f-col p{margin-top:5px;display:flex;align-items:center;gap:5px}
.connect{text-align:center;font-weight:700;letter-spacing:1px}
.social{display:flex;gap:6px;justify-content:center;margin-top:7px}
.social i{width:16px;height:16px;border-radius:50%;background:#fff;opacity:.9}
.f-list{display:flex;gap:18px;line-height:1.6}
.bottom{background:var(--footer-bottom);color:#d6e6c6;text-align:center;font-size:6.5px;height:16px;line-height:16px}
</style>
</head>
<body>
<div class="topbar"><div class="wrap">
  <span><svg width="8" height="8" viewBox="0 0 10 10"><path d="M2 1l2 2-1 1.5c.8 1.3 1.7 2.2 3 3L7.5 6l2 2-1.5 1.5C4.5 9 1 5.5.5 2.5z" fill="#fff"/></svg>123 456 7890</span>
  <span><svg width="9" height="7" viewBox="0 0 10 8"><rect x=".5" y=".5" width="9" height="7" fill="none" stroke="#fff"/><path d="M.5.5L5 4l4.5-3.5" fill="none" stroke="#fff"/></svg>admin@kreltoconsultancy.com</span>
</div></div>

<header class="header"><div class="wrap">
  <div class="logo"><i class="mark"></i><div><span class="name">KRELTO</span><span class="sub">CONSULTANCY</span></div></div>
  <nav class="nav"><a>ABOUT US</a><a>SERVICES</a><a>CLIENTS</a><a>CONTACT</a></nav>
</div></header>

<section class="hero" role="img" aria-label="Photo of a business team gathered around a laptop in a bright office">
  <div class="wrap">
    <h1>Business &amp; Management<br>Consultancy</h1>
    <span class="btn btn-green">More about us</span>
  </div>
  <div class="dots"><i></i><i></i><i></i></div>
</section>

<section class="services"><div class="wrap">
  <div class="sec-head"><h2>Services</h2><div class="search">Search<svg width="8" height="8" viewBox="0 0 10 10"><circle cx="4" cy="4" r="3" fill="none" stroke="#888" stroke-width="1.3"/><path d="M6.3 6.3L9 9" stroke="#888" stroke-width="1.3"/></svg></div></div>
  <div class="svc-grid">
    <div class="svc">
      <div class="hex"><svg viewBox="0 0 94 108"><polygon points="47,0 94,27 94,81 47,108 0,81 0,27" fill="#6aa136"/></svg><span>Finance</span></div>
      <p>Lorem ipsum dolor sit amet, consectetur adipiscing elit. Quae contraria sunt his, malane, nemo velit perpetuo tempore consili quam sapiens eterni vitae sententiam.</p>
    </div>
    <div class="svc dim">
      <div class="hex"><svg viewBox="0 0 94 108"><polygon points="47,0 94,27 94,81 47,108 0,81 0,27" fill="#c8cacb"/></svg><span>Forensic accounting</span></div>
      <p>Quo ratione ut fieri possit, recte iudicant omnes; sed nemo tamen aliquid facit sine ratione. Hoc nobis quidem placet, quod vere probamus semper in consilio.</p>
    </div>
    <div class="svc dim">
      <div class="hex"><svg viewBox="0 0 94 108"><polygon points="47,0 94,27 94,81 47,108 0,81 0,27" fill="#c8cacb"/></svg><span>Fraud prevention</span></div>
      <p>Cum autem sit in nobis ratio, qua vitam regimus, recte agendo cavemus. Sic fit ut prudentia nos semper protegat omni tempore vitae.</p>
    </div>
    <div class="svc dim">
      <div class="hex"><svg viewBox="0 0 94 108"><polygon points="47,0 94,27 94,81 47,108 0,81 0,27" fill="#c8cacb"/></svg><span>Internal control</span></div>
      <p>Ut enim ad minim veniam, quis nostrud ordo rerum servetur; ita qui recte praeest, omnia bene administrat et firma custodia tenet.</p>
    </div>
  </div>
  <div class="center"><span class="btn btn-red">More services</span></div>
</div></section>

<section class="testimonials"><div class="wrap">
  <h2>Testimonials</h2>
  <div class="quotes">
    <div class="quote"><p>Lorem ipsum dolor sit amet, consectetur adipiscing elit. Quae contraria sunt his, malane, nemo velit perpetuo tempore consili quam quoque interim enti efficere sententiam.</p><div class="who">Client Name</div></div>
    <div class="quote"><p>Quod quidem iam fit etiam in academia. Quamquam ab is philosophiam et omnes ingenuas disciplinas habemus; sed id ne cogitari quidem potest quale sit, ut non repugnet ipsum sibi. Ergo in gubernando nihil, in officio plurimum.</p><div class="who">Client Name</div></div>
    <div class="quote"><p>Apud ceteros autem philosophos, qui quaesivit aliquid, tacet. Quae non videbantur, omnia virtus, omne decus, omnis vera laus deseretur est. Voluptatem et dolorem praeter ea sententiam quidem a contemplatione natura.</p><div class="who">Client Name</div></div>
    <div class="quote"><p>Vitae autem degendae ratio maxime quidem illis placuit quieta. Quosquod porro nihilo sentimus, si omne enim si senatus. Claudii dicebat, sed sunt summa ille Aquam, dedecebat. Virtutum sed autem in dedecore partum in gratiam numerum.</p><div class="who">Client Name</div></div>
  </div>
  <div class="center"><span class="btn btn-red">More testimonials</span></div>
</div></section>

<footer class="footer"><div class="wrap">
  <div class="f-col">
    <div class="f-links"><span>Home</span><span>Sitemap</span><span>Career</span><span>Contact Us</span><span>Privacy Policy</span></div>
    <p><svg width="7" height="7" viewBox="0 0 10 10"><path d="M2 1l2 2-1 1.5c.8 1.3 1.7 2.2 3 3L7.5 6l2 2-1.5 1.5C4.5 9 1 5.5.5 2.5z" fill="#fff"/></svg>123 456 7890</p>
    <p><svg width="8" height="6" viewBox="0 0 10 8"><rect x=".5" y=".5" width="9" height="7" fill="none" stroke="#fff"/><path d="M.5.5L5 4l4.5-3.5" fill="none" stroke="#fff"/></svg>admin@kreltoconsultancy.com</p>
    <p><svg width="6" height="8" viewBox="0 0 8 10"><path d="M4 0a3.5 3.5 0 00-3.5 3.5C.5 6 4 10 4 10s3.5-4 3.5-6.5A3.5 3.5 0 004 0z" fill="#fff"/></svg>Address Name, City, USA</p>
  </div>
  <div class="connect">CONNECT WITH US<div class="social"><i></i><i></i><i></i><i></i></div></div>
  <div class="f-list">
    <div>Strategic planning<br>Facilitation<br>Quality assurance<br>Education and training<br>Investment counsel</div>
    <div>Identification and analysis<br>of management problems<br>Developing solutions<br>The implementation<br>of proposed solutions</div>
  </div>
</div></footer>
<div class="bottom">© Copyright 2013 Krelto Consultancy. All Rights Reserved.</div>
</body>
</html>
```